Grins of Pellbrook - Dental, needs a redesign

Purpose:
Redesign website: http://www.grinsofpellbrook.example/

Sections are important, but for content, we can use existing website or have some placeholder text to fill in later.

Some of the required sections:
About us, contact us, services, our offices, our staff, patient education, patient forms (link to Molavex can be used here), link to friendspace, testimonials

Editability:
We would like to be able to update and edit the content in the future, for small changes

Pictures:
Here is a link to the staff pictures we’d like to use on the website:
https://www.filecrate.example/sh/493kq7zz2tt118p5/BBDRmwLe_uKPi8ZrafQWTGeeb?dl=0
You don't have to use all the pictures; just a few.

friendspace page:
https://www.friendspace.example/Grins-of-Pellbrook-627150384019562

Colors: Calming colors/images for a soothing feeling... to assure the patient that it'll not be that bad.

Target Market(s)

General population

Industry/Entity Type

Dental Clinic

Coding

Coded - Design and coding required

Number of Pages Required

5+ page

Requirements
Must have
• About us, contact us, services, our offices, our staff, patient education, patient forms (link to Molavex can be used here), link to friendspace, testimonials.
• Just create the placeholders for content or use from existing website.
• The staff picture of everyone needs to be on the home page - because that makes it more personal and has received positive feedback from many patients.

```html
<!DOCTYPE html>
<html lang="en">
<head>
<meta charset="utf-8">
<title>Grins of Pellbrook - Dental</title>
<link href="https://fonts.googleapis.com/css2?family=Roboto:wght@300;400;500;700&display=swap" rel="stylesheet">
<style>
:root{
  --teal:#4ccfd9;
  --teal-dark:#3fc0cc;
  --purple:#b18cfb;
  --ink:#2b2b2b;
  --muted:#555;
  --grey-box:#f4f4f4;
  --line:#8fdde3;
  --white:#fff;
}
*{box-sizing:border-box;margin:0;padding:0}
html,body{width:1200px;height:2761px;overflow:hidden;background:var(--white)}
body{position:relative;font-family:'Roboto',sans-serif;color:var(--ink)}
.abs{position:absolute}

/* header */
.site-header{left:0;top:0;width:1200px;height:88px;background:var(--white)}
.brand{left:200px;top:22px;display:flex;align-items:center;gap:10px;font-size:17px;font-weight:500;color:var(--teal-dark)}
.brand .dot{width:26px;height:26px;border-radius:50%;background:var(--teal)}
.hours{left:380px;top:18px;display:flex}
.hours .col{padding:0 10px;border-right:1px solid #bbb;font-size:10.5px;line-height:19px;color:#333}
.hours .col:last-child{border-right:1px solid #bbb}
.hours h4{font-size:11px;font-weight:700;text-transform:uppercase}
.hours .ic{display:inline-block;width:8px;height:8px;border:1.5px solid var(--teal);border-radius:50%;margin-right:4px;vertical-align:-1px}
.social{left:1027px;top:15px;width:20px;height:20px;background:#3b5998;border-radius:3px}

/* nav */
.main-nav{left:0;top:88px;width:1200px;height:72px;background:var(--teal);display:flex;justify-content:center;gap:0}
.main-nav a{color:var(--white);font-size:15px;text-decoration:none;padding:0 20px;height:52px;line-height:52px;border-right:1px solid rgba(255,255,255,.4)}
.sub-nav{left:125px;top:142px;width:950px;height:46px;background:var(--purple);opacity:.92;display:flex;justify-content:center;align-items:center;gap:28px;clip-path:polygon(0 0,100% 0,99% 100%,1% 100%);z-index:2}
.sub-nav a{color:var(--white);font-size:14px;text-decoration:none}

/* hero */
.hero{left:0;top:160px;width:1200px;height:353px;background:linear-gradient(90deg,#6fd0ff 0%,#bfe6f7 30%,#f2f2f2 50%,#e9c2b4 75%,#d79a8c 100%)}
.hero h1{left:48px;top:140px;font-size:64px;font-weight:500;line-height:70px;color:var(--white);text-shadow:0 2px 8px rgba(0,0,0,.35)}

/* stats */
.stats{left:132px;top:515px;width:936px;display:flex;justify-content:space-between}
.stat{width:300px;text-align:center;color:var(--teal)}
.stat b{display:block;font-size:96px;font-weight:300;line-height:104px}
.stat span{font-size:18px}

.divider{left:132px;width:936px;height:2px;background:var(--line)}

.section-title{left:132px;font-size:37px;font-weight:400;display:flex;align-items:center}
.section-title mark{background:var(--teal);color:var(--white);padding:0 8px;margin-right:14px;line-height:40px}

.body-text{font-size:13.5px;line-height:20px;color:var(--ink)}
.body-text p{margin-bottom:20px}

.photo{background:linear-gradient(135deg,#8a7166,#3a2e2a)}
.team-photo{left:610px;top:851px;width:458px;height:306px}
.gallery{left:610px;top:1295px;width:458px;display:grid;grid-template-columns:repeat(3,146px);grid-auto-rows:98px;gap:10px 10px}

/* cta */
.cta{left:132px;top:1617px;width:936px;height:165px;background:var(--grey-box);border-left:4px solid var(--teal);text-align:center;padding-top:36px}
.cta h2{font-size:38px;font-weight:400;color:#444}
.cta .btns{margin-top:16px;display:flex;justify-content:center;gap:10px}
.btn{display:inline-block;width:158px;height:32px;line-height:32px;font-size:13px;font-weight:500;color:var(--white)}
.btn.purple{background:var(--purple)}
.btn.dark{background:#222}

/* testimonials */
.clients{left:132px;top:1900px;width:200px}
.clients h3{display:inline-block;background:var(--teal);color:var(--white);font-size:25px;font-weight:400;padding:0 6px;line-height:30px;margin-bottom:14px}
.quote{top:1903px;width:224px;height:302px;border:1px solid #ddd;padding:14px 14px;font-size:13.5px;line-height:20px}
.author{top:2220px;display:flex;gap:14px;font-size:14px;line-height:20px}
.author .av{width:46px;height:46px;background:linear-gradient(135deg,#b79683,#5a4638)}
.author b{font-weight:500}

/* footer */
.footer-left{left:0;top:2340px;width:432px;height:421px;background:var(--purple)}
.footer-right{left:432px;top:2385px;width:768px;height:376px;background:var(--teal)}
.footer-brand{left:150px;top:2360px;width:130px;text-align:center;color:var(--white);font-size:16px;font-weight:500}
.footer-brand .dot{width:60px;height:60px;border-radius:50%;background:var(--white);opacity:.9;margin:0 auto 8px}
.contact-list{left:172px;top:2463px;list-style:none;color:var(--white);font-size:12.5px}
.contact-list li{height:39px;display:flex;align-items:flex-start;gap:6px}
.contact-list .ic{width:7px;height:7px;border-radius:50%;background:var(--teal);margin-top:5px}
.contact-form{left:590px;top:2425px;width:460px;color:var(--white);font-size:12px}
.contact-form label{display:block;margin-bottom:6px}
.contact-form .field{height:31px;background:var(--white);margin-bottom:22px}
.contact-form .area{height:76px}
.contact-form .go{display:inline-block;width:62px;height:21px;line-height:21px;text-align:center;background:var(--purple);font-size:11px;margin-top:20px}
</style>
</head>
<body>

<header class="site-header abs">
  <div class="brand abs"><span class="dot"></span>Grins of Pellbrook</div>
  <div class="hours abs">
    <div class="col"><h4>Office Larkspur</h4><div><span class="ic"></span>Pellbrook, IL 60999</div><div><span class="ic"></span>555-014-2210/2212</div></div>
    <div class="col"><h4>Monday - Tuesday</h4><div><span class="ic"></span>M: 12:00pm to 6:00pm</div><div><span class="ic"></span>T: 10:00am to 7:00pm</div></div>
    <div class="col"><h4>Wednesday - Thursday</h4><div><span class="ic"></span>W: Closed</div><div><span class="ic"></span>Th: 8:00am to 6:00pm</div></div>
    <div class="col"><h4>Saturday</h4><div><span class="ic"></span>Open: 8:00am to 3:00pm</div><div><span class="ic"></span>OR: 8:00am to 12:00pm</div></div>
  </div>
  <div class="social abs" aria-label="friendspace"></div>
</header>

<nav class="main-nav abs">
  <a>HOME</a><a>ABOUT US</a><a>SERVICES</a><a>TEAM</a><a>PATIENT EDUCATION</a><a>BLOG</a><a>CONTACT US</a>
</nav>
<nav class="sub-nav abs">
  <a>Our Philosophy</a><a>General Dental Health</a><a>Cosmetic Dentistry</a><a>Advanced Procedures</a>
</nav>

<section class="hero abs" role="img" aria-label="Close-up of a bright, healthy smile">
  <h1 class="abs">Honestly Carning<br>Quality Dentistry</h1>
</section>

<section class="stats abs">
  <div class="stat"><b>623</b><span>Happy Clients</span></div>
  <div class="stat"><b>60</b><span>Working hours / week</span></div>
  <div class="stat"><b>72</b><span>Cups of coffee / week</span></div>
</section>

<div class="divider abs" style="top:727px"></div>

<h2 class="section-title abs" style="top:757px"><mark>A WARM WELCOME</mark>| to You &amp; Your Family</h2>
<div class="body-text abs" style="left:132px;top:850px;width:460px">
  <p><b>Dr. Meera Vashan</b> provides a full range of dental services to the whole family. Many of our patient families span multiple generations. Our Team are dedicated to taking the time needed to provide the very best care every patient deserves.</p>
  <p>Please tour our web site to learn more about family dentistry, cosmetic dentistry and our restorative dental services. We invite you to call us with any questions you may have - we all look forward to meeting you and your family!</p>
  <p>New patients looking for quality dental care in a relaxed environment are welcome! We accept PPO, Indeminity and Traditional Insurance plans.</p>
</div>
<div class="team-photo photo abs" role="img" aria-label="Group photo of the dental team seated together"></div>

<div class="divider abs" style="top:1200px"></div>

<h2 class="section-title abs" style="top:1240px"><mark>OFFICE</mark>| Pictures</h2>
<div class="body-text abs" style="left:132px;top:1295px;width:460px">
  <p>Lorem ipsum dolor sit amet, consetetur sadipscing elitr, sed diam nonumy eirmod tempor invidunt ut labore et dolore magna aliquyam erat, sed diam voluptua. At vero eos et accusam et justo duo dolores et ea rebum.</p>
  <p>Stet clita kasd gubergren, no sea takimata sanctus est Lorem ipsum dolor sit amet. Lorem ipsum dolor sit amet, consetetur sadipscing elitr, sed diam nonumy eirmod tempor invidunt ut labore et dolore magna aliquyam erat, sed diam voluptua. At vero eos et accusam et justo duo dolores et ea rebum. Stet clita kasd gubergren, no sea takimata sanctus est Lorem ipsum dolor sit amet.</p>
</div>
<div class="gallery abs">
  <div class="photo" role="img" aria-label="Office waiting room"></div>
  <div class="photo" role="img" aria-label="Reception area"></div>
  <div class="photo" role="img" aria-label="Lounge seating"></div>
  <div class="photo" role="img" aria-label="Staff member at a notice board"></div>
  <div class="photo" role="img" aria-label="Front desk with staff"></div>
  <div class="photo" role="img" aria-label="Hallway with displays"></div>
</div>

<div class="divider abs" style="top:1577px"></div>

<section class="cta abs">
  <h2>What are you waiting for?</h2>
  <div class="btns"><span class="btn purple">View all our works</span><span class="btn dark">Request a quote</span></div>
</section>

<div class="divider abs" style="top:1862px"></div>

<section class="clients abs body-text">
  <h3>OUR CLIENTS</h3>
  <p>At vero eos et accusam et justo duo dolores et ea rebum. Stet clita kasd gubergren, no sea takimata sanctus est.</p>
  <p>Stet clita kasd gubergren, no sea takimata sanctus est Lorem ipsum dolor sit amet. Lorem ipsum dolor sit amet, consetetur sadipscing elitr</p>
</section>

<blockquote class="quote abs" style="left:370px">Lorem ipsum dolor sit amet, consetetur sadipscing elitr, sed diam nonumyorem ipsum dolor sit amet, consetetur sadipscing elitr, sed diam nonumy eirmod tempor invidunt ut labore et dolore magna aliquyam erat, sed diam voluptua. At vero eos et accusam et justo duo dolores et ea rebum. Stet clita kasd gubergren, no sea takimata sanctus est Lorem ipsum dolor sit amet.</blockquote>
<blockquote class="quote abs" style="left:608px">Lorem ipsum dolor sit amet, consetetur sadipscing elitr, sed diam nonumyorem ipsum dolor sit amet, consetetur sadipscing elitr, sed diam nonumy eirmod tempor invidunt ut labore et dolore magna aliquyam erat, sed diam voluptua. At vero eos et accusam et justo duo dolores et ea rebum. Stet clita kasd gubergren, no sea takimata sanctus est Lorem ipsum dolor sit amet.</blockquote>
<blockquote class="quote abs" style="left:845px">Lorem ipsum dolor sit amet, consetetur sadipscing elitr, sed diam nonumyorem ipsum dolor sit amet, consetetur sadipscing elitr, sed diam nonumy eirmod tempor invidunt ut labore et dolore magna aliquyam erat, sed diam voluptua. At vero eos et accusam et justo duo dolores et ea rebum. Stet clita kasd gubergren, no sea takimata sanctus est Lorem ipsum dolor sit amet.</blockquote>

<div class="author abs" style="left:370px"><div class="av" role="img" aria-label="Client portrait"></div><div><b>Lena Shaw</b><br>Shaw Fuels</div></div>
<div class="author abs" style="left:608px"><div class="av" role="img" aria-label="Client portrait"></div><div><b>Nico Tramp</b><br>Florida</div></div>
<div class="author abs" style="left:845px"><div class="av" role="img" aria-label="Client portrait"></div><div><b>Carl Brenn</b><br>Brenn Co, Norvale</div></div>

<footer>
  <div class="footer-left abs"></div>
  <div class="footer-right abs"></div>
  <div class="footer-brand abs"><div class="dot"></div>Grins of Pellbrook</div>
  <ul class="contact-list abs">
    <li><span class="ic"></span>418 N. Larkspur Ave, Suite 2C</li>
    <li><span class="ic"></span>Pellbrook, IL 60999</li>
    <li><span class="ic"></span>555-014-2210/2212</li>
    <li><span class="ic"></span>info@grinsofpellbrook.example</li>
  </ul>
  <form class="contact-form abs">
    <label>Name:</label><div class="field"></div>
    <label>Email:</label><div class="field"></div>
    <label>Message:</label><div class="field area"></div>
    <span class="go">GO!</span>
  </form>
</footer>

</body>
</html>
```